Postcard design for Intellectual Property Professional Conference

Seeking design for 5.5" by 8.5" postcard mailer about a conference on tax and finance issues for international IP management. Attendees are lawyers and financial executives. Draft language is attached.

Target Market(s)

The project should have the attached picture of Boston with the caption "Courtesy of the Harborline Meeting & Travelers Council"

Industry/Entity Type

Finance

```html
<!DOCTYPE html>
<html lang="en">
<head>
<meta charset="UTF-8">
<title>Intellectual Property in Developing Growth Markets — Conference Postcard</title>
<link href="https://fonts.googleapis.com/css2?family=Montserrat:wght@700;800&family=Source+Sans+3:wght@400;600;700&display=swap" rel="stylesheet">
<style>
  :root {
    --navy: #0d4a8c;
    --royal: #1565b8;
    --sky: #3fb0ea;
    --pale: #e3f3fb;
    --white: #ffffff;
    --ink: #1d1d1f;
    --photo-warm: #b88a6e;
    --photo-cool: #8fb3cc;
  }
  * { box-sizing: border-box; margin: 0; padding: 0; }
  html, body { width: 776px; height: 1200px; overflow: hidden; background: var(--white); }
  .postcard {
    position: relative;
    width: 776px;
    height: 1200px;
    overflow: hidden;
    background: linear-gradient(180deg, #ffffff 28%, var(--pale) 70%, #cfe9f6 100%);
    font-family: "Source Sans 3", Arial, sans-serif;
    color: var(--ink);
  }
  .hero-art { position: absolute; left: 0; top: 0; width: 776px; height: 360px; }
  .hero-title {
    position: absolute;
    top: 14px;
    left: 196px;
    width: 570px;
    font-family: "Montserrat", Arial, sans-serif;
    font-weight: 800;
    font-size: 50px;
    line-height: 56px;
    color: var(--white);
    text-shadow: 0 2px 4px rgba(0,0,0,0.35);
  }
  .hero-title span { display: block; }
  .hero-title .line-two { padding-left: 82px; }
  .save-badge { position: absolute; left: 368px; top: 196px; width: 396px; height: 214px; }
  .save-badge__text {
    position: absolute;
    left: 378px;
    top: 220px;
    width: 370px;
    text-align: center;
    font-family: "Montserrat", Arial, sans-serif;
    font-weight: 800;
    color: var(--white);
    transform: rotate(-9deg);
    transform-origin: center;
  }
  .save-badge__lead { font-size: 36px; line-height: 44px; }
  .save-badge__amount { font-size: 52px; line-height: 58px; }
  .event-title {
    position: absolute;
    top: 346px;
    left: 10px;
    font-family: "Montserrat", Arial, sans-serif;
    font-weight: 800;
    font-size: 40px;
    line-height: 47px;
    color: var(--navy);
    letter-spacing: -0.3px;
  }
  .event-date {
    position: absolute;
    top: 492px;
    left: 0;
    width: 776px;
    padding-left: 212px;
    font-weight: 700;
    font-size: 24px;
    letter-spacing: -0.5px;
    color: var(--royal);
  }
  .event-intro {
    position: absolute;
    top: 520px;
    left: 10px;
    width: 760px;
    font-size: 20.5px;
    line-height: 27px;
    text-align: justify;
  }
  .event-intro p + p { margin-top: 18px; }
  .topics-band { position: absolute; left: 0; top: 850px; width: 776px; height: 350px; }
  .topics {
    position: absolute;
    top: 862px;
    left: 18px;
    width: 750px;
    color: var(--white);
  }
  .topics__heading { font-weight: 700; font-size: 23px; letter-spacing: -0.4px; margin-bottom: 6px; }
  .topics__columns { display: flex; gap: 26px; }
  .topics__list {
    list-style: none;
    font-size: 16.4px;
    line-height: 20.1px;
    letter-spacing: 1.1px;
  }
  .topics__list--left { width: 362px; }
  .topics__list--right { width: 340px; }
  .topics__list li { position: relative; padding-left: 11px; }
  .topics__list li::before { content: "•"; position: absolute; left: 0; top: 0; }
</style>
</head>
<body>
<div class="postcard">
  <svg class="hero-art" viewBox="0 0 776 360" aria-hidden="false">
    <defs>
      <linearGradient id="harbor" x1="0" y1="0" x2="0" y2="1">
        <stop offset="0" stop-color="#c9d6df"/>
        <stop offset="0.45" stop-color="#a98f7c"/>
        <stop offset="0.7" stop-color="#7d8e96"/>
        <stop offset="1" stop-color="#b0866a"/>
      </linearGradient>
      <linearGradient id="sweep" x1="0" y1="0" x2="1" y2="0">
        <stop offset="0" stop-color="#bfe4f6"/>
        <stop offset="1" stop-color="#eef8fd"/>
      </linearGradient>
    </defs>
    <path role="img" aria-label="Photograph of the Boston waterfront with a tall ship, harbor walk and downtown towers"
          d="M0 0 H776 V250 C600 300 350 330 200 338 C120 342 50 336 0 330 Z" fill="url(#harbor)"/>
    <path d="M0 0 H150 C90 20 40 60 0 110 Z" fill="url(#sweep)"/>
    <path d="M0 330 C80 342 200 342 330 330 C500 314 650 280 776 240 V360 H0 Z" fill="url(#sweep)"/>
  </svg>

  <h1 class="hero-title"><span>Increasing Profits</span><span class="line-two">&amp; Protecting</span></h1>

  <svg class="save-badge" viewBox="0 0 396 214" aria-hidden="true">
    <defs>
      <radialGradient id="badgeFill" cx="0.45" cy="0.45" r="0.6">
        <stop offset="0" stop-color="#1a6dc4"/>
        <stop offset="1" stop-color="#0c3f86"/>
      </radialGradient>
    </defs>
    <ellipse cx="198" cy="107" rx="192" ry="101" transform="rotate(-9 198 107)" fill="url(#badgeFill)" stroke="#4cc0ef" stroke-width="7"/>
  </svg>
  <div class="save-badge__text">
    <div class="save-badge__lead">Register Early<br>and Save up to</div>
    <div class="save-badge__amount">$300</div>
  </div>

  <h2 class="event-title">INTELLECTUAL<br>PROPERTY IN<br>DEVELOPING GROWTH MARKETS</h2>
  <div class="event-date">BOSTON MARCH 24 &amp; 25, 2016</div>

  <div class="event-intro">
    <p>You are cordially invited to attend a comprehensive and practical day and a half conference to examine the tax and legal structuring strategies for increasing profits from Intellectual properties while protecting these important assets when doing business in fast growing developing markets. Intellectual property assets include some of the most important assets of most companies: their patents, trade marks, copyrights, brand names and licensing agreements.</p>
    <p>Senior tax, legal and financial experts will provide a comprehensive analysis of the legal issues, recent tax &amp; regulatory developments, skills and structuring strategies necessary to maximize profits from IP Migrating IP assets to low tax jurisdiction will also be covered along with dealing with issues of piracy, counterfeiting, infringement and other legal challenges to a company’s IP.</p>
  </div>

  <svg class="topics-band" viewBox="0 0 776 350" preserveAspectRatio="none" aria-hidden="true">
    <defs>
      <linearGradient id="bandFill" x1="0" y1="0" x2="0" y2="1">
        <stop offset="0" stop-color="#0f4f96"/>
        <stop offset="0.5" stop-color="#1a6fc0"/>
        <stop offset="1" stop-color="#2f8fd6"/>
      </linearGradient>
    </defs>
    <path d="M0 12 C200 4 500 2 776 14 V350 H0 Z" fill="url(#bandFill)"/>
    <path d="M0 12 C200 4 500 2 776 14" fill="none" stroke="#7fcdf1" stroke-width="3"/>
  </svg>

  <section class="topics">
    <h3 class="topics__heading">TOPICS TO BE COVERED INCLUDE:</h3>
    <div class="topics__columns">
      <ul class="topics__list topics__list--left">
        <li>Market trends in IP tax &amp; legal structures</li>
        <li>Proposed US Tax changes and regulatory developments outside the US including European and OECD developments affecting IP, patent box, base erosion and profit splitting(BEPS)</li>
        <li>Overview of the IP landscape in key developing growth markets such as China, India, Brazil, Korea, South Africa,<br>Mexico and other developing markets outside the US.</li>
        <li>Restructuring and Migration of IP Assets to Tax Advantaged Jurisdictions</li>
      </ul>
      <ul class="topics__list topics__list--right">
        <li>Legal issues including litigation, arbitration and use of government assistance to protect IP values in key developing markets.</li>
        <li>Monetizing IP assets and rights in regard to divestitures, spin offs, split offs, M&amp;A, transfers of ownership and securitizations in developing growth markets</li>
        <li>Special Tax Planning and Legal Considerations for IP in Particular Sectors such as Biopharmaceutical, International Sports Licensing, High Tech, Consumer Brands, and Manufacuring</li>
      </ul>
    </div>
  </section>
</div>
</body>
</html>
```